Brandt Family Motto/Mission Statement

We are creating a poster to be hung in our home with several purpose statements for our family (last name Brandt, and "The Brandt Family" should be included in the poster prominently). The text that we want included is in the attached file.

Our kids range in age from 8 to 17, so we are looking for something that is homey and cheerful, but fairly bold and oriented to older kids (and not so much younger kids).

I've attached a couple of example poster/statements that we generally like. Overall color scheme could include blues and greens and possibly some brown.

Anticipated size of this poster would be 18"x24" with a portrait orientation.

```html
<!DOCTYPE html>
<html lang="en">
<head>
<meta charset="utf-8">
<title>The Brandt Family – Family Mission Statement</title>
<link rel="stylesheet" href="https://fonts.googleapis.com/css2?family=Tinos&family=Michroma&display=swap">
<style>
  :root {
    --deep-blue: #3c46a4;
    --mid-blue: #3a5fb4;
    --teal-glow: #2f93a6;
    --green-glow: #5fb25a;
    --ink-white: #ffffff;
    --accent-green: #b9d34a;
    --accent-blue: #5ec8ea;
    --title-fill: #1e2f6e;
    --title-stroke: #3fd0f2;
  }
  html, body {
    margin: 0;
    padding: 0;
    overflow: hidden;
    background: #ffffff;
  }
  .poster {
    position: relative;
    width: 855px;
    height: 1200px;
    overflow: hidden;
    background: radial-gradient(ellipse 60% 55% at 50% 52%, var(--teal-glow) 0%, var(--mid-blue) 55%, var(--deep-blue) 100%);
    font-family: "Tinos", "Times New Roman", serif;
  }
  .artwork {
    position: absolute;
    left: 0;
    top: 0;
    width: 855px;
    height: 1200px;
  }
  .side-title {
    position: absolute;
    left: 36px;
    top: 296px;
    transform: rotate(-90deg);
    transform-origin: left top;
    font-family: "Michroma", sans-serif;
    font-size: 15px;
    letter-spacing: 1px;
    color: var(--ink-white);
    white-space: nowrap;
  }
  .values {
    position: absolute;
    left: 0;
    top: 0;
    width: 855px;
    margin: 0;
    padding: 0;
    list-style: none;
  }
  .value {
    position: absolute;
    left: 0;
    width: 855px;
    text-align: center;
    font-size: 25px;
    line-height: 1;
    color: var(--ink-white);
    white-space: nowrap;
  }
  .value .key {
    font-size: 34px;
  }
  .key.green { color: var(--accent-green); }
  .key.blue { color: var(--accent-blue); }
  .value-learn { top: 240px; }
  .value-positive { top: 340px; }
  .value-kindness { top: 435px; }
  .value-adventure { top: 535px; }
  .value-fit { top: 633px; }
  .value-humor { top: 731px; }
  .value-right { top: 831px; }
  .main-title {
    position: absolute;
    left: 0;
    top: 1104px;
    width: 855px;
    margin: 0;
    text-align: center;
    font-family: "Michroma", sans-serif;
    font-weight: 400;
    font-size: 46px;
    letter-spacing: 3px;
    color: var(--title-fill);
    -webkit-text-stroke: 1.5px var(--title-stroke);
    white-space: nowrap;
  }
</style>
</head>
<body>
<main class="poster">
  <svg class="artwork" viewBox="0 0 855 1200" role="img" aria-label="Flowing dark ribbon swirl with silhouettes of children cartwheeling and jumping, glowing green and teal">
    <defs>
      <radialGradient id="glow-green" cx="50%" cy="50%" r="50%">
        <stop offset="0%" stop-color="var(--green-glow)" stop-opacity="0.75"/>
        <stop offset="100%" stop-color="var(--green-glow)" stop-opacity="0"/>
      </radialGradient>
      <radialGradient id="glow-brown" cx="50%" cy="50%" r="50%">
        <stop offset="0%" stop-color="#4a3a3a" stop-opacity="0.45"/>
        <stop offset="100%" stop-color="#4a3a3a" stop-opacity="0"/>
      </radialGradient>
    </defs>
    <ellipse cx="360" cy="200" rx="260" ry="190" fill="url(#glow-brown)"/>
    <ellipse cx="420" cy="560" rx="220" ry="300" fill="url(#glow-green)"/>
    <ellipse cx="195" cy="910" rx="150" ry="190" fill="url(#glow-green)"/>
    <ellipse cx="630" cy="910" rx="150" ry="160" fill="url(#glow-green)"/>
  </svg>

  <div class="side-title">THE BRANDT FAMILY</div>

  <ul class="values">
    <li class="value value-learn">We love to <span class="key green">learn</span> new things.</li>
    <li class="value value-positive">We look at life through a <span class="key blue">positive</span> lens.</li>
    <li class="value value-kindness"><span class="key green">Kindness</span> guides our words and deeds.</li>
    <li class="value value-adventure">We create <span class="key blue">adventure</span> and choose experiences over things.</li>
    <li class="value value-fit">We commit to be <span class="key green">fit</span>.</li>
    <li class="value value-humor">Our days are brightened by a <span class="key blue">sense of humor</span>.</li>
    <li class="value value-right">We <span class="key green">do what is right</span> even when no one is watching.</li>
  </ul>

  <h1 class="main-title">THE BRANDT FAMILY</h1>
</main>
</body>
</html>
```